Design my site www.briefmarkpost.com

So here is what I am thinking in terms of design:

https://plenvo.com

https://www.skylarkjetways.com

http://quillweekly.com/harbor-tower-plaza/

I want the theme to be white and blue (royal blue). I attached a paint picture of what I would like the site to look like in terms of placing the text. Generally, what I like about the sites above is that they are simple, you can navigate easily and have some kind of idea of what's going on by looking at the center (picture and motto). Let's establish a clear understanding of how the functional part of the site would look like. Please see the picture attached.

I want to keep it simple: On top would be the Name 'BRIEFMARK post", somewhere to the right on top on the page would be 'Sign in" button.

In the center would be a picture (maybe a video) with the Motto (on top of it all in capital) OBSERVE NAVIGATE DECIDE and below would be the "sign up now"

Below the picture (like on quillweekly.com site) or to the left on top of the page would be "About Us', "Press" "Contact Us' buttons.

Then once the user gets to his page his got 3 tabs " Press Headlines", "Events", " Briefings".

we would keep the same format I only have on the site, but separate for every Tab.

I do not want the user to get distracted. I also want him to be able to access the page though mobile phone and be able to get automatic updates just like Zentro Pings without having to sign in daily.

The landing page must be minimalist yet with business/corporate feel where users can navigate easily and a "what you see is what you get" approach. You want an image or video (personally I prefer the video.. it does capture the users attention instantly, as long as it is an interesting video), with your taglines in it.

Sections available to public: About Us, Contact Us, Landing Page with Signup Option

Private: Public Sections + User Account Page, Tabs for (Events, Press Headlines, Briefings)

Target Market(s)

PR/media monitoring/diplomatic community

Coding

Coded - Design and coding required

Number of Pages Required

1 page

Font styles to use
Serif
Sans Serif

Colors
0255a3
ec1f27

Requirements
Must have
• a simple landing page, that is user friendly.
Nice to have
• a video with the explanation of how to navigate the site
Should not have
• too many colors, graphs etc.

```html
<!DOCTYPE html>
<html lang="en">
<head>
<meta charset="utf-8">
<title>BRIEFMARK post — Briefings</title>
<link rel="stylesheet" href="https://fonts.googleapis.com/css2?family=Open+Sans:wght@400;600&family=Roboto:wght@400&family=Roboto+Condensed:wght@400&display=swap">
<style>
  :root {
    --blue: #2e93c4;
    --blue-dark: #1f7fb0;
    --ink: #3a3a3a;
    --muted: #555;
    --panel: #f4f4f4;
    --line: #dddddd;
    --footer: #f7f7f7;
    --white: #ffffff;
  }
  * { box-sizing: border-box; margin: 0; padding: 0; }
  html, body { width: 1200px; height: 896px; overflow: hidden; background: var(--white); font-family: "Open Sans", sans-serif; color: var(--ink); }
  .page { position: relative; width: 1200px; height: 896px; }

  .hero {
    position: absolute; left: 0; top: 0; width: 1200px; height: 258px;
    background: linear-gradient(180deg, #3c4a63 0%, #26334a 35%, #1b2435 70%, #2a2a33 100%);
    border-top: 2px solid var(--blue);
  }
  .brand {
    position: absolute; left: 99px; top: 40px; width: 320px; height: 56px;
    border: 2px solid var(--white);
    display: flex; align-items: center; justify-content: center;
    color: var(--white); font-weight: 600; font-size: 29px; letter-spacing: 0.5px;
  }
  .sign-in {
    position: absolute; left: 982px; top: 51px; width: 84px; height: 33px;
    background: var(--blue); border: 1px solid #9fd3ee; border-radius: 3px;
    color: var(--white); font-weight: 600; font-size: 13px;
    display: flex; align-items: center; justify-content: center;
  }
  .menu-toggle { position: absolute; left: 1078px; top: 58px; }

  .tabs { position: absolute; left: 99px; top: 296px; width: 1001px; height: 43px; border-bottom: 1px solid var(--blue); }
  .tab { position: absolute; top: 0; height: 42px; display: flex; align-items: center; justify-content: center; font-size: 15.5px; font-weight: 600; color: #444; }
  .tab-press { left: 0; width: 198px; }
  .tab-events { left: 250px; width: 142px; }
  .tab-briefings { left: 435px; width: 207px; background: var(--blue); color: var(--white); }

  .panel { position: absolute; left: 98px; top: 338px; width: 1002px; height: 381px; background: var(--panel); border: 1px solid var(--line); border-top: none; }
  .photo-frame { position: absolute; left: 40px; top: 43px; width: 433px; height: 295px; background: var(--white); border: 1px solid #ddd; padding: 7px; }
  .photo { width: 100%; height: 100%; background: linear-gradient(120deg, #c8a57a 0%, #e5ddd0 35%, #2b3547 70%, #dcdcdc 100%); }

  .briefing { position: absolute; left: 513px; top: 56px; width: 450px; }
  .briefing h1 { font-family: "Roboto", sans-serif; font-weight: 400; font-size: 33px; color: var(--ink); letter-spacing: 0.5px; }
  .briefing h2 { font-family: "Roboto Condensed", sans-serif; font-weight: 400; font-size: 21px; color: #333; margin-top: 6px; margin-left: -2px; }
  .briefing p { font-size: 11.5px; line-height: 23px; color: var(--muted); margin-top: 15px; }
  .checklist { list-style: none; margin-top: 14px; }
  .checklist li { display: flex; align-items: center; font-size: 13px; height: 26.5px; color: #333; }
  .checklist svg { margin-right: 12px; flex: none; }

  .footer { position: absolute; left: 0; top: 785px; width: 1200px; height: 111px; background: var(--footer); border-top: 1px solid #e6e6e6; }
  .footer-nav { position: absolute; left: 99px; top: 35px; font-size: 13px; display: flex; gap: 12px; }
  .footer-nav a { color: var(--blue); text-decoration: none; }
  .footer-nav span { color: #333; }
  .copyright { position: absolute; left: 98px; top: 63px; font-size: 13px; color: #333; }
  .social { position: absolute; left: 928px; top: 34px; display: flex; gap: 9px; }
  .social span { width: 28px; height: 28px; border-radius: 50%; background: var(--blue); display: block; }
</style>
</head>
<body>
<div class="page">
  <header class="hero" role="img" aria-label="Dusk skyline photograph of a city with towers">
    <div class="brand">BRIEFMARK POST</div>
    <div class="sign-in">SIGN IN</div>
    <svg class="menu-toggle" width="23" height="20" viewBox="0 0 23 20" aria-label="Menu">
      <rect x="0" y="0" width="23" height="4" fill="#fff"/>
      <rect x="0" y="8" width="23" height="4" fill="#fff"/>
      <rect x="0" y="16" width="23" height="4" fill="#fff"/>
    </svg>
  </header>

  <nav class="tabs">
    <div class="tab tab-press">PRESS HEADLINES</div>
    <div class="tab tab-events">EVENTS</div>
    <div class="tab tab-briefings">BRIEFINGS</div>
  </nav>

  <section class="panel">
    <div class="photo-frame">
      <div class="photo" role="img" aria-label="Photograph of a businessman writing at a desk in front of bookshelves"></div>
    </div>
    <div class="briefing">
      <h1>BRIEFINGS</h1>
      <h2>Duis aute irure dolor in reprehenderit</h2>
      <p>Nemo enim ipsam voluptatem quia voluptas sit aspernatur aut odit aut fugit, sed quia consequuntur magni dolores eos qui ratione voluptatem sequi nesciunt. Neque porro quisquam est, qui dolorem ipsum quia dolor sit amet, consectetur, adipisci velit, sed quia non numquam eius modi tempora incidunt ut labore</p>
      <ul class="checklist">
        <li><svg width="11" height="11" viewBox="0 0 11 11"><rect width="11" height="11" rx="2" fill="#2e93c4"/><path d="M2.5 5.6l2 2 4-4.2" stroke="#fff" stroke-width="1.6" fill="none"/></svg>Duis aute irure dolor in reprehenderit in voluptate</li>
        <li><svg width="11" height="11" viewBox="0 0 11 11"><rect width="11" height="11" rx="2" fill="#2e93c4"/><path d="M2.5 5.6l2 2 4-4.2" stroke="#fff" stroke-width="1.6" fill="none"/></svg>Neque porro quisquam est, qui dolorem</li>
        <li><svg width="11" height="11" viewBox="0 0 11 11"><rect width="11" height="11" rx="2" fill="#2e93c4"/><path d="M2.5 5.6l2 2 4-4.2" stroke="#fff" stroke-width="1.6" fill="none"/></svg>Quis autem vel eum iure reprehenderit</li>
      </ul>
    </div>
  </section>

  <footer class="footer">
    <div class="footer-nav"><a href="#">ABOUT US</a><span>/</span><a href="#">PRESS</a><span>/</span><a href="#">CONTACT US</a></div>
    <div class="copyright">2016 © Copyrights BRIEFMARK post.All Rights Reserved</div>
    <div class="social" aria-label="Social links">
      <span></span><span></span><span></span><span></span><span></span>
    </div>
  </footer>
</div>
</body>
</html>
```